I need a flyer made , the flyer can be one page or two pages or three pages . I will be posting this on Instagram and social media platforms. I am a luxury home builder , I am looking to hire a construction project manager . Below are some examples and ideas what can be on the flyer

We’re looking for a construction project manager who’s passionate about building luxury homes at the highest standards
We’re hiring construction project manager
* Experience 5+ years in residential project management with a strong portfolio of completed homes.
* location : Bergen County NJ
* excellent leadership skills, leads teams with confidence and clarity
* communicates seamlessly with architects , engineers, designers and clients
*knows how to manage budgets and timelines without compromising quality
*solves problems with a positive solution first mindset
* pays attention to every detail because in luxury the small things are the big things

Apply now , link in bio or DM to connect.

My logo is attached, my web site www.ridgelanebuilders.com
My style is modern but still warm and inviting. I like a clean classy look .
Updates

Please don’t add any images of chairs or people to the flyer , I do not want people on my flyer. Do not add standard images of offices and houses , we are luxury builders , we build homes over 2 million dollars. Keep a classy , simple modern look . High end .

You can add a white hard hat with my logo on it for a image , this is a suggestion does not have to be on my flyer ,

```html
<!DOCTYPE html>
<html lang="en">
<head>
<meta charset="UTF-8">
<title>Ridgelane Builders — Hiring Construction Project Manager</title>
<link rel="stylesheet" href="https://fonts.googleapis.com/css2?family=Archivo:wdth,wght@62..125,300..800&display=swap">
<style>
  :root {
    --ink: #000000;
    --paper: #ffffff;
    --silk-light: #5a5a5a;
    --silk-mid: #262626;
    --accent-red: #d0100f;
    --muted: #d9d9d9;
  }
  * { margin: 0; padding: 0; box-sizing: border-box; }
  html, body { width: 1200px; height: 1200px; overflow: hidden; background: var(--ink); }
  body { font-family: "Archivo", Arial, sans-serif; color: var(--paper); }

  .flyer { position: relative; width: 1200px; height: 1200px; overflow: hidden; background: var(--ink); }

  .silk-backdrop {
    position: absolute; inset: 0;
    background:
      radial-gradient(ellipse 160px 260px at 700px 300px, rgba(120,120,120,0.55), transparent 70%),
      radial-gradient(ellipse 420px 120px at 620px 560px, rgba(90,90,90,0.45), transparent 70%),
      radial-gradient(ellipse 300px 160px at 420px 760px, rgba(110,110,110,0.45), transparent 70%),
      radial-gradient(ellipse 260px 420px at 420px 1050px, rgba(80,80,80,0.5), transparent 70%),
      radial-gradient(ellipse 500px 300px at 950px 1050px, rgba(50,50,50,0.45), transparent 70%),
      radial-gradient(ellipse 600px 240px at 300px 120px, rgba(40,40,40,0.6), transparent 70%),
      var(--ink);
  }

  .brand { position: absolute; top: 118px; left: 0; width: 1200px; text-align: center; }
  .brand-name { font-size: 52px; font-weight: 300; letter-spacing: 2px; font-stretch: 100%; }
  .brand-sub { margin-top: 10px; font-size: 17px; font-weight: 300; letter-spacing: 4px; color: var(--muted); }

  .headline { position: absolute; left: 0; width: 1200px; text-align: center; font-stretch: 112%; line-height: 1; }
  .headline-lead { top: 326px; left: 18px; font-size: 98px; font-weight: 400; letter-spacing: -7px; }
  .headline-main { top: 398px; left: 0; font-size: 262px; font-weight: 600; letter-spacing: -12px; }

  .role { position: absolute; left: 683px; top: 752px; font-size: 34px; line-height: 40px; letter-spacing: -1.5px; font-stretch: 108%; }
  .role-kind { font-weight: 400; }
  .role-title { font-weight: 800; }

  .requirements { position: absolute; left: 81px; top: 851px; width: 460px; list-style: none; }
  .requirements li {
    position: relative; padding-left: 33px; margin-bottom: 12px;
    font-size: 25px; line-height: 32px; letter-spacing: -1.3px; font-weight: 400;
  }
  .requirements li svg { position: absolute; left: 0; top: 9px; }

  .apply-ribbon { position: absolute; left: 680px; top: 959px; width: 194px; height: 60px; }
  .apply-ribbon span {
    position: absolute; inset: 0; display: flex; align-items: center; justify-content: center;
    padding-right: 14px; font-size: 23px; font-weight: 800; letter-spacing: -1px;
  }

  .contact { position: absolute; left: 683px; top: 1040px; }
  .contact-line { display: flex; align-items: center; gap: 14px; font-size: 30px; letter-spacing: -1.3px; line-height: 40px; }
  .contact-line svg { flex: none; }
</style>
</head>
<body>
  <main class="flyer">
    <div class="silk-backdrop" role="img" aria-label="Flowing dark black and grey silk fabric backdrop"></div>

    <header class="brand">
      <div class="brand-name">RIDGELANE</div>
      <div class="brand-sub">builders</div>
    </header>

    <h1>
      <span class="headline headline-lead">WE ARE</span>
      <span class="headline headline-main">HIRING</span>
    </h1>

    <h2 class="role">
      <span class="role-kind">CONSTRUCTION</span><br>
      <span class="role-title">PROJECT MANAGER</span>
    </h2>

    <ul class="requirements">
      <li><svg width="12" height="16" viewBox="0 0 12 16"><path d="M2 1l7 7-7 7" fill="none" stroke="#fff" stroke-width="2.4"/></svg>5+ yrs residential experience in home building.</li>
      <li><svg width="12" height="16" viewBox="0 0 12 16"><path d="M2 1l7 7-7 7" fill="none" stroke="#fff" stroke-width="2.4"/></svg>Excellent leadership skills.</li>
      <li><svg width="12" height="16" viewBox="0 0 12 16"><path d="M2 1l7 7-7 7" fill="none" stroke="#fff" stroke-width="2.4"/></svg>Effectively manages budgets and timelines while maintaining quality standards.</li>
      <li><svg width="12" height="16" viewBox="0 0 12 16"><path d="M2 1l7 7-7 7" fill="none" stroke="#fff" stroke-width="2.4"/></svg>Pays attention to every detail</li>
    </ul>

    <div class="apply-ribbon">
      <svg width="194" height="60" viewBox="0 0 194 60"><polygon points="0,0 165,0 194,30 165,60 0,60 14,30" fill="var(--accent-red)"/></svg>
      <span>Apply Now</span>
    </div>

    <div class="contact">
      <div class="contact-line">
        <svg width="18" height="24" viewBox="0 0 18 24"><path d="M9 0C4 0 0 4 0 9c0 6.5 9 15 9 15s9-8.5 9-15C18 4 14 0 9 0z" fill="#fff"/><circle cx="9" cy="9" r="3.4" fill="#000"/></svg>
        <span>Bergen County NJ</span>
      </div>
      <div class="contact-line">
        <svg width="18" height="20" viewBox="0 0 18 20"><path d="M1 1l15 6-6 2 7 7-3 3-7-7-2 6z" fill="#fff"/></svg>
        <span>ridgelanebuilders.com</span>
      </div>
    </div>
  </main>
</body>
</html>
```